Hypothetical Customer Lifecycle

Need a poster to show the lifecycle of a student going through university.

There are three main stages of the lifecycle, it also needs to visually loop back in some way to the start from the end of the 3rd stage.

1) Prospect – Strategy is to Acquire
There are three main sub experiences within this stage which are
a. Decide
b. Apply
c. On board
Within the Prospect stage we also need to show some Needs and Pain Points as below
Needs
• Validation on choices from peers or family
• Clear direction on choices
Pain Points
• Not sure where to start
• Poor navigation and information architecture

2) Current – Strategy is to Engage
a. Commence
b. Study
c. Complete
Within the Current stage we also need to show some Needs and Pain Points as below
Needs
• Access to peer groups and faculty
• Flexibility in modes of learning
Pain Points
• Quality of faculty engagement can vary
• Online tools are hard to use

3) Alumni – Strategy is to Retain
a. Graduate
b. Job Seek
c. Network
Needs
• Options to further career
• Competency based learning
Pain Points
• Lots of irrelevant emails and mail
• Struggle to relate to Alumni programs

Target Market(s)

Exec level, technology managers

Industry/Entity Type

Education

Font styles to use
Sans Serif

Colors
1696d0
ecf7fb
3176b5
ffffff

Requirements
Must have
• Simple visual elements
Should not have
• Try and avoid arrows, chevrons anything that strongly implies a process.

```html
<!DOCTYPE html>
<html lang="en">
<head>
<meta charset="utf-8">
<title>Hypothetical Customer Lifecycle</title>
<link rel="stylesheet" href="https://fonts.googleapis.com/css2?family=Roboto:wght@400;500;700&display=swap">
<style>
  :root {
    --bg: #d5dfe1;
    --white: #ffffff;
    --grey-text: #7a7f82;
    --grey-dark: #6d7274;
    --prospect: #f15a29;
    --prospect-light: #fbb040;
    --current: #0f8489;
    --current-light: #22b573;
    --current-top: #0e9aa6;
    --alumni: #0d6fba;
    --alumni-light: #29abe2;
    --accent-blue: #1696d0;
  }
  html, body {
    margin: 0;
    padding: 0;
    width: 1200px;
    height: 750px;
    overflow: hidden;
    background: var(--bg);
  }
  .lifecycle-poster {
    display: block;
    width: 1200px;
    height: 750px;
    font-family: "Roboto", Arial, sans-serif;
  }
  .stage-title { font-size: 42px; font-weight: 700; }
  .stage-title.prospect { fill: var(--prospect); }
  .stage-title.current { fill: var(--current); }
  .stage-title.alumni { fill: var(--alumni); }
  .strategy { font-size: 20px; fill: var(--grey-text); }
  .strategy tspan.verb { font-weight: 700; fill: var(--grey-dark); }
  .note-heading { font-size: 20px; font-weight: 700; }
  .note-heading.prospect { fill: var(--prospect); }
  .note-heading.current { fill: var(--current); }
  .note-heading.alumni { fill: var(--alumni); }
  .note-line { font-size: 16.5px; fill: var(--grey-text); }
  .bullet.prospect { fill: var(--prospect); }
  .bullet.current { fill: var(--current); }
  .bullet.alumni { fill: var(--alumni); }
  .step { font-size: 20px; fill: var(--white); font-weight: 500; text-anchor: middle; }
  .step-divider { stroke: var(--white); stroke-width: 1.2; fill: none; }
  .hub-light { font-size: 24px; fill: #8c9194; text-anchor: middle; }
  .hub-bold { font-size: 28px; font-weight: 700; fill: #7c8184; text-anchor: middle; }
  .orbit { fill: none; stroke: var(--white); stroke-width: 2; stroke-dasharray: 1 6; stroke-linecap: round; opacity: .9; }
</style>
</head>
<body>
<svg class="lifecycle-poster" viewBox="0 0 1280 800" xmlns="http://www.w3.org/2000/svg" role="img" aria-label="Hypothetical customer lifecycle: Prospect, Current and Alumni stages">
  <defs>
    <clipPath id="disc-clip"><circle cx="640" cy="395" r="265"/></clipPath>
    <linearGradient id="prospect-fill" x1="0" y1="1" x2="1" y2="0">
      <stop offset="0" stop-color="var(--prospect)"/>
      <stop offset="1" stop-color="var(--prospect-light)"/>
    </linearGradient>
    <linearGradient id="current-fill" x1="0" y1="0" x2="0.6" y2="1">
      <stop offset="0" stop-color="var(--current-top)"/>
      <stop offset="1" stop-color="var(--current-light)"/>
    </linearGradient>
    <linearGradient id="alumni-fill" x1="0" y1="0" x2="1" y2="0.3">
      <stop offset="0" stop-color="var(--alumni-light)"/>
      <stop offset="1" stop-color="var(--alumni)"/>
    </linearGradient>
  </defs>

  <!-- connectors -->
  <g class="connectors">
    <polygon points="600,100 630,100 640,140 608,140" fill="var(--prospect)"/>
    <polygon points="860,520 905,535 900,570 850,555" fill="var(--current)"/>
    <polygon points="420,545 445,560 420,610 395,600" fill="var(--alumni)"/>
  </g>

  <!-- outer ring -->
  <circle cx="640" cy="395" r="322" fill="var(--white)"/>

  <!-- stage segments -->
  <g class="stage-disc" clip-path="url(#disc-clip)">
    <polygon class="segment-prospect" fill="url(#prospect-fill)"
      points="640,395 560,455 478,475 432,548 200,700 200,50 640,50 640,130 673,212 640,290"/>
    <polygon class="segment-current" fill="url(#current-fill)"
      points="640,395 640,290 673,212 640,130 640,50 1100,50 1100,700 850,550 763,530 720,455"/>
    <polygon class="segment-alumni" fill="url(#alumni-fill)"
      points="640,395 720,455 763,530 850,550 1100,700 1100,800 200,800 200,700 432,548 478,475 560,455"/>
  </g>
  <circle class="orbit" cx="640" cy="395" r="245"/>

  <!-- hub -->
  <g class="hub">
    <path d="M640 283 A112 112 0 0 0 545 455 L640 395 Z" fill="var(--prospect)"/>
    <path d="M640 283 A112 112 0 0 1 735 455 L640 395 Z" fill="var(--current)"/>
    <path d="M545 455 A112 112 0 0 0 735 455 L640 395 Z" fill="var(--alumni)"/>
    <circle cx="640" cy="395" r="99" fill="var(--white)"/>
    <circle cx="616" cy="347" r="8" fill="var(--prospect)"/>
    <circle cx="639" cy="347" r="8" fill="var(--current-top)"/>
    <circle cx="662" cy="347" r="8" fill="var(--alumni)"/>
    <text class="hub-light" x="640" y="385">Hypothetical</text>
    <text class="hub-bold" x="640" y="416">Customer</text>
    <text class="hub-bold" x="640" y="447">Lifecycle</text>
  </g>

  <!-- steps -->
  <g class="steps-prospect">
    <text class="step" x="470" y="303">Decide</text>
    <path class="step-divider" d="M422 314 H466 L470 318 L474 314 H518"/>
    <text class="step" x="470" y="347">Apply</text>
    <path class="step-divider" d="M422 358 H466 L470 362 L474 358 H518"/>
    <text class="step" x="470" y="390">On board</text>
  </g>
  <g class="steps-current">
    <text class="step" x="812" y="347">Commence</text>
    <path class="step-divider" d="M764 358 H808 L812 362 L816 358 H860"/>
    <text class="step" x="812" y="391">Study</text>
    <path class="step-divider" d="M764 402 H808 L812 406 L816 402 H860"/>
    <text class="step" x="812" y="435">Complete</text>
  </g>
  <g class="steps-alumni">
    <text class="step" x="640" y="533">Graduate</text>
    <path class="step-divider" d="M592 544 H636 L640 548 L644 544 H688"/>
    <text class="step" x="640" y="577">Job Seek</text>
    <path class="step-divider" d="M592 588 H636 L640 592 L644 588 H688"/>
    <text class="step" x="640" y="621">Network</text>
  </g>

  <!-- stage badges -->
  <g class="badge-prospect">
    <circle cx="595" cy="62" r="51" fill="var(--white)"/>
    <circle cx="595" cy="62" r="39" fill="none" stroke="var(--prospect)" stroke-width="6"/>
    <circle cx="595" cy="62" r="20" fill="var(--grey-dark)" role="img" aria-label="Prospect icon: head with question mark"/>
  </g>
  <g class="badge-current">
    <circle cx="935" cy="557" r="51" fill="var(--white)"/>
    <circle cx="935" cy="557" r="39" fill="none" stroke="var(--current)" stroke-width="6"/>
    <path d="M935 580 C928 568 921 560 921 551 A14 14 0 0 1 949 551 C949 560 942 568 935 580 Z" fill="var(--grey-dark)"/>
    <circle cx="935" cy="551" r="5" fill="var(--white)"/>
    <ellipse cx="935" cy="581" rx="14" ry="4" fill="none" stroke="var(--grey-dark)" stroke-width="2"/>
  </g>
  <g class="badge-alumni">
    <circle cx="400" cy="630" r="51" fill="var(--white)"/>
    <circle cx="400" cy="630" r="39" fill="none" stroke="var(--alumni)" stroke-width="6"/>
    <circle cx="400" cy="630" r="20" fill="var(--grey-dark)" role="img" aria-label="Alumni icon: graduate in cap"/>
  </g>

  <!-- stage titles -->
  <text class="stage-title prospect" x="528" y="62" text-anchor="end">Prospect</text>
  <text class="strategy" x="528" y="88" text-anchor="end">Strategy is to <tspan class="verb">Acquire</tspan></text>

  <text class="stage-title current" x="993" y="562">Current</text>
  <text class="strategy" x="993" y="589">Strategy is to <tspan class="verb">Engage</tspan></text>

  <text class="stage-title alumni" x="340" y="634" text-anchor="end">Alumni</text>
  <text class="strategy" x="340" y="661" text-anchor="end">Strategy is to <tspan class="verb">Retain</tspan></text>

  <!-- prospect notes -->
  <g class="notes-prospect" text-anchor="end">
    <text class="note-heading prospect" x="344" y="180">Needs</text>
    <text class="note-line" x="344" y="202"><tspan class="bullet prospect">•</tspan> Validation on choices</text>
    <text class="note-line" x="344" y="224">from peers or family</text>
    <text class="note-line" x="344" y="245"><tspan class="bullet prospect">•</tspan> Clear direction on choices</text>
    <text class="note-heading prospect" x="297" y="311">Pain Points</text>
    <text class="note-line" x="297" y="334"><tspan class="bullet prospect">•</tspan> Not sure where to start</text>
    <text class="note-line" x="297" y="355"><tspan class="bullet prospect">•</tspan> Poor navigation and</text>
    <text class="note-line" x="297" y="377">information architecture</text>
  </g>

  <!-- current notes -->
  <g class="notes-current">
    <text class="note-heading current" x="936" y="156">Needs</text>
    <text class="note-line" x="936" y="178"><tspan class="bullet current">•</tspan> Access to peer groups</text>
    <text class="note-line" x="946" y="199">and faculty</text>
    <text class="note-line" x="936" y="221"><tspan class="bullet current">•</tspan> Flexibility in modes</text>
    <text class="note-line" x="946" y="242">of learning</text>
    <text class="note-heading current" x="985" y="311">Pain Points</text>
    <text class="note-line" x="985" y="333"><tspan class="bullet current">•</tspan> Quality of faculty</text>
    <text class="note-line" x="995" y="354">engagement can vary</text>
    <text class="note-line" x="985" y="376"><tspan class="bullet current">•</tspan> Online tools are hard to use</text>
  </g>

  <!-- alumni notes -->
  <g class="notes-alumni" text-anchor="middle">
    <text class="note-heading alumni" x="477" y="725">Needs</text>
    <text class="note-line" x="477" y="747"><tspan class="bullet alumni">•</tspan> Options to further career</text>
    <text class="note-line" x="486" y="769"><tspan class="bullet alumni">•</tspan> Competency based learning</text>
    <text class="note-heading alumni" x="847" y="725">Pain Points</text>
    <text class="note-line" x="847" y="747"><tspan class="bullet alumni">•</tspan> Lots of irrelevant emails and mail</text>
    <text class="note-line" x="850" y="769"><tspan class="bullet alumni">•</tspan> Struggle to relate to Alumni programs</text>
  </g>
</svg>
</body>
</html>
```